Harbor Crest Seminar Postcard Design

I need a postcard designed that is 5.5" x 8.5". Color front and back with space for an address block and postal indicia. I will provide the bullet points and copy. I need assistance with the layout, organization and perhaps a couple of images, etc. This postcard will drive individuals to a web site to register for a 90-minute seminar teaching them how to minimize or eliminate their income taxes during retirement.
Target Market(s)
Married Couples, ages 50 - 70. Successful and affluent. People that appreciate and value professional advice and relationships.
Requirements
Must have
- Bright and Bold.  Compelling and attention grabbing.
Call to action #1 - Go to website immediately for further information.
Call to action #2 - Call the office immediately to register.

```html
<!DOCTYPE html>
<html lang="en">
<head>
<meta charset="utf-8">
<title>Harbor Crest Seminar Postcard</title>
<link href="https://fonts.googleapis.com/css2?family=Lato:wght@400;700&family=Oswald:wght@400&display=swap" rel="stylesheet">
<style>
  :root {
    --backdrop: #151515;
    --card: #ffffff;
    --ink: #2b2b2b;
    --muted: #6e6e6e;
    --accent: #f5a623;
    --band: #f7a221;
    --deep-red: #a50e0e;
    --rule: #bdbdbd;
  }
  * { margin: 0; padding: 0; box-sizing: border-box; }
  html, body { width: 1200px; height: 1100px; overflow: hidden; background: var(--backdrop); }
  body { position: relative; font-family: "Lato", Arial, sans-serif; color: var(--ink); }

  .card { position: absolute; left: 188px; width: 799px; background: var(--card); overflow: hidden; }
  .card-back { top: 18px; height: 516px; }
  .card-front { top: 556px; height: 516px; width: 798px; }

  /* Back side */
  .points { position: absolute; left: 24px; top: 22px; width: 404px; list-style: none; }
  .points li { position: relative; padding-left: 17px; font-size: 15.2px; line-height: 18.4px; }
  .points li::before { content: ""; position: absolute; left: 0; top: 6px; width: 9px; height: 9px; border-radius: 50%; background: var(--accent); }
  .points .point-1 { margin-bottom: 12px; }
  .points .point-2 { margin-bottom: 16px; }
  .points .point-3 { margin-bottom: 19px; }
  .quote, .tagline { position: absolute; left: 26px; width: 358px; font-size: 15.2px; line-height: 18.4px; color: var(--muted); }
  .quote { top: 382px; }
  .tagline { top: 455px; }
  .divider { position: absolute; left: 434px; top: 65px; width: 1px; height: 397px; background: var(--rule); }
  .stamp-box { position: absolute; left: 678px; top: 60px; width: 81px; height: 80px; border: 1px solid var(--rule); }
  .address-lines { position: absolute; left: 448px; top: 227px; width: 316px; }
  .address-lines span { display: block; height: 1px; background: var(--rule); margin-bottom: 24.6px; }

  /* Front side */
  .headline { position: absolute; top: 20px; left: 0; width: 100%; text-align: center; white-space: nowrap; font-family: "Oswald", "Arial Narrow", sans-serif; font-weight: 400; font-size: 40px; line-height: 50px; color: #111; }
  .subhead { position: absolute; top: 72px; left: 20px; right: 20px; text-align: center; font-weight: 700; font-size: 15.6px; line-height: 23.5px; color: #222; }
  .photo { position: absolute; top: 136px; left: 0; width: 100%; height: 230px; background: linear-gradient(90deg, #b88a2a 0%, #d9b26a 25%, #e8c9a8 50%, #c9b9a8 70%, #d2b24a 100%); }
  .cta-band { position: absolute; top: 366px; left: 0; width: 100%; height: 150px; background: var(--band); text-align: center; font-weight: 700; font-size: 17px; line-height: 23.5px; color: #fff; padding-top: 10px; }
  .cta-band .register { color: #111; font-size: 16.5px; }
  .cta-band .web { color: var(--deep-red); }
  .cta-band .phone-line { color: var(--deep-red); margin-top: 19px; }
</style>
</head>
<body>

<section class="card card-back">
  <ul class="points">
    <li class="point-1">Are you upset or angry at the government for confiscating more and more of your hard earned money??</li>
    <li class="point-2">Many financial experts agree that income taxes need to double (that's right, double!!) in the next ten years or else we will fly head over heels into another financial disaster??</li>
    <li class="point-3">How would you like to dramatically decrease or even eliminate your income taxes during your retirement years?? (It is possible!!)</li>
    <li>This information is critical to your retirement plan!! Reducing or eliminating income taxes during retirement can make your financial nest egg last much longer and since Americans are living longer than ever before, you should be doing everything possible to learn about this critically important subject.</li>
  </ul>
  <p class="quote">“I personally guarantee – when you attend this seminar, your view of the complex world of Wealth and Taxation will be dramatically different”</p>
  <p class="tagline">More Knowledge, Increased Confidence and More Capability</p>
  <div class="divider"></div>
  <div class="stamp-box"></div>
  <div class="address-lines"><span></span><span></span><span></span><span></span><span></span></div>
</section>

<section class="card card-front">
  <h1 class="headline">The Harbor Crest Seminar A Free Educational Seminar</h1>
  <p class="subhead">A Unique, One-Of-A-Kind Program Reveals Little Known Secrets Used By America’s Wealthiest<br>Families To Reduce And Even Eliminate Their Income Taxes During Their Retirement Years</p>
  <div class="photo" role="img" aria-label="Photo of a smiling retired couple embracing outdoors among autumn leaves"></div>
  <div class="cta-band">
    <p class="register">Register Today!!</p>
    <p>Visit <span class="web">www.HarborCrestWealthGroup.Com</span> right away to learn about upcoming dates,<br>times and locations</p>
    <p class="phone-line">Call our office to register immediately (555) 014-2290</p>
  </div>
</section>

</body>
</html>
```